BUSINESS CARD DESIGN

NAME- TODD MARSHECK
PHONE NUMER - 808- 555-0147
EMAIL- OFFICE@VORN-GRADEWORKS.COM
BACK OF CARD- SPEACIALIZES IN LAND CLEARING, FORESTRY MUCLHING AND EXCAVATION

Contact Information for Business Card

NAME- TODD MARSHECK PHONE NUMER - 808- 555-0147 EMAIL- OFFICE@VORN-GRADEWORKS.COM BACK OF CARD- SPEACIALIZES IN LAND CLEARING , MUCLHING AND EXCAVATION

```html
<!DOCTYPE html>
<html lang="en">
<head>
<meta charset="utf-8">
<title>Vorn Gradeworks Business Card</title>
<link rel="stylesheet" href="https://fonts.googleapis.com/css2?family=Montserrat:wght@400;500&family=Lato:wght@400&family=Roboto+Condensed:wght@500&display=swap">
<style>
  :root {
    --page: #2a2b2d;
    --card: #141516;
    --white: #f2f2f2;
    --silver: #d6d6d6;
    --gold: #f5ad17;
    --gold-soft: rgba(245, 173, 23, 0.85);
  }
  * { margin: 0; padding: 0; box-sizing: border-box; }
  html, body { width: 1200px; height: 952px; overflow: hidden; background: var(--page); }
  .canvas { position: relative; width: 1200px; height: 952px; }

  .card {
    position: absolute;
    left: 232px;
    width: 736px;
    height: 420px;
    background: var(--card);
    box-shadow: 0 10px 30px rgba(0,0,0,0.5);
    overflow: hidden;
  }
  .card-front { top: 40px; }
  .card-back { top: 492px; }

  .brand {
    position: absolute;
    display: flex;
    align-items: center;
    gap: 12px;
    font-family: "Montserrat", sans-serif;
    font-weight: 500;
    color: var(--silver);
    letter-spacing: 2px;
    white-space: nowrap;
  }
  .brand-dot { border-radius: 50%; border: 2px solid var(--silver); }
  .card-front .brand { left: 360px; top: 92px; font-size: 20px; }
  .card-front .brand-dot { width: 40px; height: 40px; }
  .card-back .brand { left: 50%; top: 118px; transform: translateX(-50%); font-size: 30px; }
  .card-back .brand-dot { width: 58px; height: 58px; }

  .gold-rule {
    position: absolute;
    height: 1px;
    background: linear-gradient(90deg, transparent, var(--gold-soft) 50%, transparent);
  }
  .card-front .rule-top { left: 200px; top: 190px; width: 420px; }
  .card-front .rule-bottom { left: 120px; top: 316px; width: 440px; }
  .card-back .rule-mid { left: 120px; top: 250px; width: 500px; }

  .holder {
    position: absolute;
    left: 100px;
    top: 212px;
    text-align: right;
    width: 260px;
  }
  .holder-name {
    font-family: "Montserrat", sans-serif;
    font-weight: 400;
    font-size: 25px;
    color: var(--white);
    letter-spacing: 0.5px;
  }
  .holder-name .surname { color: var(--gold); font-weight: 500; }
  .holder-role {
    font-family: "Lato", sans-serif;
    font-size: 15px;
    color: var(--white);
    margin-top: 6px;
  }
  .divider {
    position: absolute;
    left: 378px;
    top: 208px;
    width: 1px;
    height: 86px;
    background: var(--silver);
  }
  .contact {
    position: absolute;
    left: 398px;
    top: 214px;
    list-style: none;
    font-family: "Lato", sans-serif;
    font-size: 16px;
    color: var(--white);
  }
  .contact li { display: flex; align-items: center; gap: 12px; height: 34px; }
  .contact-icon {
    width: 24px; height: 24px;
    background: var(--gold);
    border-radius: 4px;
    display: flex; align-items: center; justify-content: center;
  }

  .services {
    position: absolute;
    left: 0; right: 0;
    top: 268px;
    display: flex;
    justify-content: center;
    gap: 44px;
    list-style: none;
    font-family: "Roboto Condensed", sans-serif;
    font-weight: 500;
    font-size: 15px;
    color: var(--white);
    letter-spacing: 0.3px;
  }
  .services li { display: flex; align-items: center; gap: 6px; }
  .services li::before {
    content: "";
    width: 5px; height: 5px;
    border-radius: 50%;
    background: var(--gold);
  }
</style>
</head>
<body>
<main class="canvas">
  <section class="card card-front" aria-label="Card front">
    <div class="brand"><span class="brand-dot"></span>VORN GRADEWORKS LLC</div>
    <div class="gold-rule rule-top"></div>
    <div class="holder">
      <p class="holder-name">TODD <span class="surname">MARSHECK</span></p>
      <p class="holder-role">Managing Director</p>
    </div>
    <div class="divider"></div>
    <ul class="contact">
      <li>
        <span class="contact-icon">
          <svg width="14" height="14" viewBox="0 0 24 24"><path fill="#fff" d="M6.6 10.8a15.1 15.1 0 0 0 6.6 6.6l2.2-2.2c.3-.3.7-.4 1-.2 1.1.4 2.3.6 3.6.6.6 0 1 .4 1 1V20c0 .6-.4 1-1 1A17 17 0 0 1 3 4c0-.6.4-1 1-1h3.5c.6 0 1 .4 1 1 0 1.3.2 2.5.6 3.6.1.3 0 .7-.2 1z"/></svg>
        </span>
        808- 555-0147
      </li>
      <li>
        <span class="contact-icon">
          <svg width="14" height="14" viewBox="0 0 24 24"><path fill="none" stroke="#fff" stroke-width="2" d="M3 6h18v12H3z M3 6l9 7 9-7"/></svg>
        </span>
        office@vorn-gradeworks.com
      </li>
    </ul>
    <div class="gold-rule rule-bottom"></div>
  </section>

  <section class="card card-back" aria-label="Card back">
    <div class="brand"><span class="brand-dot"></span>VORN GRADEWORKS LLC</div>
    <div class="gold-rule rule-mid"></div>
    <ul class="services">
      <li>SPEACIALIZES IN LAND CLEARING</li>
      <li>MUCLHING AND EXCAVATION</li>
    </ul>
  </section>
</main>
</body>
</html>
```